Interfaith organization needs a poster advertising event for youth

We need a poster advertising our annual Lantern Gathering and Summit, where youth of all different religions come together for dialogue, friendship, fun, art, and musical performances. The poster should be have a front advertising the event, and the back should have more detailed descriptions of the event and submissions. It should be fun and eye catching!

Target Market(s)

Youth and Religious Organizations

Industry/Entity Type

Festival

Font styles to use
Serif

Requirements
Must have
• Pictures, poster-feel, contact information, etc. Logos of Bright Harbor Allies and Crossroads Young Leaders Circle of Maple Valley

```html
<!DOCTYPE html>
<html lang="en">
<head>
<meta charset="utf-8">
<title>Lantern Gathering and Summit Poster</title>
<link href="https://fonts.googleapis.com/css2?family=Montserrat:wght@800;900&family=Alegreya+Sans+SC:wght@700;800&family=Arimo:wght@400;700&display=swap" rel="stylesheet">
<style>
  :root {
    --backdrop: #e9e4dc;
    --navy: #1c2a8c;
    --royal: #2f49c9;
    --violet: #5a2fb0;
    --title-violet: #7a3fe0;
    --gold: #f7d330;
    --white: #ffffff;
    --orange: #f0582e;
    --cyan: #36c4ec;
    --green: #6cc83e;
    --purple: #8a39b8;
    --band: #f08a2a;
    --ink: #1b2466;
  }
  * { box-sizing: border-box; margin: 0; padding: 0; }
  html, body { width: 1200px; height: 789px; overflow: hidden; }
  body { background: var(--backdrop); position: relative; font-family: "Arimo", Arial, sans-serif; }

  .front, .back { position: absolute; top: 45px; height: 695px; box-shadow: 0 4px 14px rgba(0,0,0,.35); overflow: hidden; }
  .front { left: 55px; width: 510px;
    background:
      radial-gradient(ellipse at 50% 22%, rgba(120,220,255,.75) 0%, rgba(70,120,240,.35) 30%, transparent 60%),
      linear-gradient(180deg, #3d6fe0 0%, var(--royal) 35%, var(--navy) 70%, var(--violet) 100%);
  }
  .front .rays { position: absolute; inset: 0; }

  .title-main { position: absolute; top: 16px; left: 0; width: 100%; text-align: center;
    font-family: "Montserrat", sans-serif; font-weight: 900; font-size: 54px; letter-spacing: 1px;
    color: var(--title-violet); -webkit-text-stroke: 1.5px #d8c8ff; }
  .title-sub { position: absolute; top: 80px; left: 20px; width: 470px; text-align: center;
    font-family: "Montserrat", sans-serif; font-weight: 800; font-size: 24px; line-height: 28px;
    color: var(--gold); text-transform: uppercase; }

  .tagline { position: absolute; top: 226px; left: 20px; width: 282px;
    font-family: "Alegreya Sans SC", sans-serif; font-weight: 800; color: var(--white);
    font-size: 27px; line-height: 31px; text-align: center; }
  .theme { position: absolute; top: 348px; left: 36px; width: 265px;
    font-family: "Alegreya Sans SC", sans-serif; font-weight: 800; color: var(--gold);
    font-size: 27px; line-height: 31px; }
  .date { position: absolute; top: 432px; left: 36px; color: var(--white);
    font-family: "Arimo", sans-serif; font-size: 19px; line-height: 25px; font-weight: 700; }
  .date .time { font-size: 21px; }
  .venue { position: absolute; top: 494px; left: 36px; width: 220px; color: var(--gold);
    font-family: "Arimo", sans-serif; font-weight: 700; font-size: 18px; line-height: 23px; }
  .address { position: absolute; top: 550px; left: 36px; color: var(--white);
    font-size: 17px; line-height: 22px; }

  .front-photo { position: absolute; left: 307px; width: 193px; height: 100px; border: 2px solid var(--white); }
  .front-photo.one { top: 245px; background: linear-gradient(135deg, #8a6b5a, #c9c1b6 50%, #5a4236); }
  .front-photo.two { top: 384px; background: linear-gradient(135deg, #2a2426, #9a8c88 50%, #d8d0cc); }
  .front-photo.three { top: 524px; background: linear-gradient(135deg, #b98d72, #6e3b30 50%, #d6cfc6); }

  .partners { position: absolute; top: 607px; left: 35px; display: flex; gap: 32px; align-items: center; }
  .partner { background: var(--white); height: 66px; display: flex; align-items: center; gap: 6px; padding: 0 8px;
    font-family: "Arimo", sans-serif; font-weight: 700; font-size: 11px; line-height: 13px; color: var(--navy); }
  .partner.council { width: 78px; text-align: center; justify-content: center; font-size: 9px; line-height: 11px; }
  .partner.allies { width: 120px; font-size: 16px; line-height: 18px; }
  .partner .dot { width: 14px; height: 14px; border-radius: 50%; background: var(--navy); flex: none; }

  .back { left: 617px; width: 530px; background: linear-gradient(180deg, #2d56d6, #1a2f9a); }
  .box { position: absolute; left: 4px; width: 276px; padding: 6px 8px; color: var(--white);
    font-size: 9.2px; line-height: 11.4px; overflow: hidden; }
  .box h2 { font-family: "Arimo", sans-serif; font-weight: 700; font-size: 12px; margin-bottom: 3px; }
  .box p + p { margin-top: 6px; }
  .box.intro { top: 12px; height: 108px; background: var(--orange); font-size: 9.8px; line-height: 11.8px; }
  .box.summit { top: 133px; height: 247px; background: var(--cyan); }
  .box.gathering { top: 383px; height: 140px; background: var(--green); }
  .box.gallery { top: 527px; height: 138px; background: var(--purple); }

  .back-photo { position: absolute; }
  .back-photo.drummer { left: 280px; top: 0; width: 250px; height: 185px; background: linear-gradient(135deg, #e8e6e8, #b2293a 45%, #d9c3ad); }
  .back-photo.speakers { left: 280px; top: 188px; width: 250px; height: 222px; background: linear-gradient(135deg, #5b3a2c, #cfc5bd 55%, #7b5444); }
  .back-photo.percussion { left: 280px; top: 413px; width: 110px; height: 252px; background: linear-gradient(135deg, #d9d4cc, #5a3a2b 55%, #a6988a); }
  .back-photo.dancer { left: 392px; top: 413px; width: 138px; height: 252px; background: linear-gradient(135deg, #d7cdc4, #c8252a 50%, #f2c81e); }

  .contact-band { position: absolute; left: 0; bottom: 0; width: 100%; height: 30px; background: var(--band);
    display: flex; align-items: center; justify-content: flex-end; padding-right: 50px; gap: 6px;
    font-family: "Arimo", sans-serif; font-weight: 700; font-size: 17px; color: var(--ink); }
</style>
</head>
<body>

<section class="front">
  <svg class="rays" width="510" height="695" viewBox="0 0 510 695" aria-hidden="true">
    <g fill="#ffffff" opacity=".07">
      <polygon points="255,150 120,0 170,0"/>
      <polygon points="255,150 230,0 280,0"/>
      <polygon points="255,150 340,0 390,0"/>
      <polygon points="255,150 450,0 510,20"/>
      <polygon points="255,150 0,40 0,90"/>
      <polygon points="255,150 510,120 510,170"/>
      <polygon points="255,150 0,200 0,250"/>
    </g>
  </svg>

  <h1 class="title-main">CROSSROADS</h1>
  <p class="title-sub">Young Leaders Circle of Maple Valley’s 13th Annual Lantern Gathering and Summit</p>

  <p class="tagline">Teens Expressing<br>Their Faith Through<br>Art, Music &amp; Dialogue</p>
  <p class="theme">This Year’s Theme<br>“Is Religion Cool?”</p>
  <p class="date">Sunday, March 19, 2017<br><span class="time">11:00 AM to 5:00 PM</span></p>
  <p class="venue">The Meridian<br>Community Hall</p>
  <p class="address">4150 Linden Grove Ave.<br>Maple Valley, CA 90000</p>

  <div class="front-photo one" role="img" aria-label="Photo of four teens singing together from song sheets"></div>
  <div class="front-photo two" role="img" aria-label="Photo of smiling teens making heart shapes with their hands"></div>
  <div class="front-photo three" role="img" aria-label="Photo of teens playing harmonium, drums and sitar"></div>

  <div class="partners">
    <div class="partner council">Crossroads Young Leaders Circle of Maple Valley</div>
    <div class="partner allies"><span class="dot"></span>Bright Harbor Allies</div>
  </div>
</section>

<section class="back">
  <div class="box intro">
    <p>All high school age faith groups are invited to come and join with 150 to 175 other high school students from various faith traditions to participate in the Crossroads Young Leaders Circle of Maple Valley’s Annual Interfaith Youth Summit. More than ever, our county and world need young leaders who are willing to learn from each other and build stronger communities!</p>
  </div>

  <div class="box summit">
    <h2>LANTERN SUMMIT</h2>
    <p>The purpose of this Interfaith Youth Summit is to bring together young people from diverse ethnic, cultural, and religious backgrounds, and to engage them in dialogue. True dialogue is a conversation on a common subject between two or more persons of differing points of view and/or backgrounds. We feel that this commitment to dialogue will affect relationships in a constructive way in our places of worship and in our community.<br>The summit itself involves having eight religiously diverse high school-age students, one adult, and youth leader around each table to discuss common questions. Our youth leaders act as facilitators, but it is stressed that it is the students we want to hear from.</p>
    <p>RSVP for our LANTERN SUMMIT by February 19th, 2017</p>
  </div>

  <div class="box gathering">
    <h2>LANTERN GATHERING</h2>
    <p>The summit will be followed by the Lantern Gathering where families of the participants are welcomed to join. The Gathering will include musical performances of all types from diverse religious communities. The differing performing arts include but are not limited to singing, dancing, instrumental music, storytelling, etc.</p>
    <p>To Participate in our Lantern Gathering (Music, Song, Dance), RSVP by February 25th, 2017</p>
  </div>

  <div class="box gallery">
    <h2>ART GALLERY</h2>
    <p>This event will include and Art Gallery display of students’ work, highlighting their expressions of faith, and artwork promoting learning, understanding, leadership, and service. Art includes any painting, illustration, sculpture, photography or other visual art.</p>
    <p>Art Work for our Art Gallery must be submitted by: March 10th, 2017</p>
  </div>

  <div class="back-photo drummer" role="img" aria-label="Photo of a teen in a turban playing tabla drums"></div>
  <div class="back-photo speakers" role="img" aria-label="Photo of two teens speaking to a seated audience"></div>
  <div class="back-photo percussion" role="img" aria-label="Photo of a teen playing drums"></div>
  <div class="back-photo dancer" role="img" aria-label="Photo of a dancer in a red and yellow costume"></div>

  <div class="contact-band">
    <svg width="16" height="16" viewBox="0 0 24 24" aria-hidden="true"><circle cx="12" cy="12" r="11" fill="none" stroke="#1b2466" stroke-width="2"/><path d="M8 6c1 0 2 2.5 2 3s-1 1-1 1.5 2 3.5 3.5 3.5c.5 0 1-1 1.5-1s3 1 3 2-1 2-2 2C11 18 6 13 6 8c0-1 1-2 2-2z" fill="#1b2466"/></svg>
    <span>(555) 014-2290 | clyc-mv.org</span>
  </div>
</section>

</body>
</html>
```